Business Card Design Project

We need a business card design for an existing company in Dallas/Fort Worth that is expanding services and re-branding. We are changing the name from Bristow Commercial Cleaning to Kelmont Facility Services. We are expanding from only commercial cleaning to include complete commercial landscape and facility maintenance services, too.

As stated, we offer a package of services that includes landscape, janitorial and facility services, which is largely unique in the industry.

We would like a design that communicates trust/partnership with a professional, corporate image, but not necessarily using the standard white business card. We would like a design that perhaps uses darker blues or perhaps a gray background, but we are open to other ideas. We might also be interested in a double-sided design - maybe with our logo on the back, printed on a gray background?

We will probably stick with the attached logo, but if you've got another inspired idea....

Target Market(s)

Property managers, commercial real estate professionals, corporate executives

Industry/Entity Type

Landscape

Requirements
Should not have
• Not interested in old style fonts.

```html
<!DOCTYPE html>
<html lang="en">
<head>
<meta charset="utf-8">
<title>Kelmont Facility Services — Business Card</title>
<link rel="stylesheet" href="https://fonts.googleapis.com/css2?family=Source+Sans+3:wght@400;600&display=swap">
<style>
  :root {
    --backdrop: #2a2a2c;
    --card-light: #8a8a8c;
    --card-mid: #6e6e70;
    --card-dark: #4e4e50;
    --ink-dark: #2b2b2d;
    --ink-light: #f2f2f2;
    --ink-soft: #d9d9d9;
    --blue-bright: #1f6fe0;
    --blue-deep: #0d2f78;
    --blue-accent: #2a7cf0;
  }
  * { box-sizing: border-box; margin: 0; padding: 0; }
  html, body { width: 1200px; height: 1000px; overflow: hidden; }
  body {
    background: var(--backdrop);
    font-family: "Source Sans 3", "Helvetica Neue", Arial, sans-serif;
    position: relative;
  }
  .card {
    position: absolute;
    width: 630px;
    height: 360px;
    border-radius: 4px;
    overflow: hidden;
    background: radial-gradient(ellipse at 55% 45%, var(--card-light) 0%, var(--card-mid) 55%, var(--card-dark) 100%);
    box-shadow: 0 14px 30px rgba(0,0,0,0.45);
  }
  .card--back { left: 80px; top: 60px; }
  .card--front { left: 490px; top: 560px; }

  /* Back side: company name */
  .back-title {
    position: absolute;
    left: 0; right: 0; top: 140px;
    text-align: center;
    color: var(--ink-dark);
    font-weight: 600;
  }
  .company-name {
    font-size: 36px;
    letter-spacing: 2px;
    text-transform: uppercase;
    line-height: 1.1;
  }
  .company-tagline {
    font-size: 16px;
    margin-top: 10px;
  }

  /* Front side */
  .front-title {
    position: absolute; left: 28px; top: 40px;
    color: var(--ink-light);
    font-weight: 600;
  }
  .front-title .company-name { font-size: 22px; letter-spacing: 1px; }
  .front-title .company-tagline { font-size: 9px; margin-top: 4px; }

  .person {
    position: absolute; right: 24px; top: 20px;
    color: var(--ink-soft);
    font-size: 30px; line-height: 1.1;
    text-align: center;
  }

  .growth-graphic {
    position: absolute; right: 30px; top: 120px;
    width: 150px; height: 100px;
    background: linear-gradient(40deg, rgba(42,124,240,0) 15%, rgba(42,124,240,0.5) 65%, rgba(42,124,240,0.1) 100%);
  }

  .service-list {
    position: absolute; left: 70px; top: 168px;
    list-style: none; color: var(--ink-light); font-size: 14px; line-height: 22px;
  }
  .service-list li { display: flex; align-items: center; gap: 6px; }
  .service-list li::before {
    content: ""; width: 6px; height: 6px; background: var(--blue-accent);
  }

  .band-stripe {
    position: absolute; left: 0; right: 0; top: 268px; height: 20px;
    background: var(--blue-bright);
  }
  .contact-bar {
    position: absolute; left: 0; right: 0; top: 288px; bottom: 0;
    background: linear-gradient(180deg, var(--blue-deep), #0a2360);
    display: flex; align-items: center; justify-content: space-between;
    padding: 0 22px; color: var(--ink-light); font-size: 17px;
  }
</style>
</head>
<body>

  <section class="card card--back" aria-label="Business card, back side">
    <div class="back-title">
      <div class="company-name">Kelmont Facility Services</div>
      <div class="company-tagline">One Source For Landscape, Janitorial and Facility Maintenance</div>
    </div>
  </section>

  <section class="card card--front" aria-label="Business card, front side">
    <div class="front-title">
      <div class="company-name">Kelmont Facility Services</div>
      <div class="company-tagline">One Source For Landscape, Janitorial and Facility Maintenance</div>
    </div>

    <div class="person">
      <div class="person-name">Daniel Whitaker</div>
      <div class="person-role">Manager</div>
    </div>

    <div class="growth-graphic" role="img" aria-label="Blue rising arrows graphic"></div>

    <ul class="service-list">
      <li>commercial cleaning</li>
      <li>commercial landscape</li>
      <li>janitorial services</li>
      <li>facility maintenance services</li>
    </ul>

    <div class="band-stripe"></div>
    <div class="contact-bar">
      <span>Phone: (555)214.3081</span>
      <span>Email: dwhit@kelmont.com</span>
      <span>Cell: 555.736.1942</span>
    </div>
  </section>

</body>
</html>
```